Thornel Injection System Postcard Design

I own a lawn care company that does mostly landscape maintenance work. I recently got certified to inject trees with environmentally safe Thornel products including fertilizers, insecticides, fungicides, and antibiotics. There are no companies in my area offering tree care services and the sticky honeydew mess from insects in trees is pretty nasty during the summer months. It covers and stains any and all surfaces underneath these trees including parked cars. I will be using every door direct mail to see who is interested in these services in my area. Sketches attached are what I had in mind, but anything will be considered. Open to any fonts and colors. Backgrounds should be "natural" in appearance (not necessarily nature themed). Reds should be avoided unless it is used to emphasize key words.Target demographic: home/ property owners, business managers, city governmentMISSING ON SKETCHES: general environmental facts- no groundwater contamination, closed system, no spraying, safe around people, pets, wildlife, and pools.

Colors
6b449b
0355a3
f37122
9bcb3c

Requirements
Must have
• Green: #00ff00
• Blue:#0000ff
• Purple: #8600b3
• Orange:#ff6600

```html
<!DOCTYPE html>
<html lang="en">
<head>
<meta charset="utf-8">
<title>Thornel Tree Care Postcard</title>
<link href="https://fonts.googleapis.com/css2?family=Oswald:wght@400;500;600&family=Open+Sans:wght@400;600;700&display=swap" rel="stylesheet">
<style>
  :root {
    --stage: #2b2b2b;
    --green-deep: #4f9a1c;
    --green-mid: #7fbf2e;
    --green-light: #9bcb3c;
    --cream: #fbfdf4;
    --mint: #e6f1d2;
    --ink-green: #2c4a17;
    --ink-grey: #3c3f44;
    --curve: #2a2a2a;
    --purple: #6b449b;
    --blue: #0355a3;
    --orange: #f37122;
    --lime: #9bcb3c;
    --white: #ffffff;
  }
  * { margin: 0; padding: 0; box-sizing: border-box; }
  html, body { width: 900px; height: 1200px; overflow: hidden; }
  body { background: var(--stage); position: relative; font-family: "Open Sans", Arial, sans-serif; }

  .postcard {
    position: absolute; left: 62px; width: 776px; height: 423px; overflow: hidden;
    background: radial-gradient(ellipse at 55% 70%, var(--cream) 0%, var(--mint) 100%);
    box-shadow: 0 4px 14px rgba(0,0,0,.6);
  }
  .postcard--front { top: 145px; }
  .postcard--back { top: 643px; }
  .postcard__art { position: absolute; inset: 0; }

  .headline {
    position: absolute; left: 42px; font-family: "Oswald", "Arial Narrow", sans-serif;
    font-weight: 500; text-transform: uppercase; line-height: 1; white-space: nowrap;
  }
  .headline--lead { top: 38px; font-size: 34px; color: var(--white); letter-spacing: .2px; }
  .headline--question { top: 77px; font-size: 34px; color: var(--ink-grey); }
  .headline--offer { top: 121px; font-size: 19px; font-weight: 400; color: var(--white); line-height: 26px; }

  .indicia {
    position: absolute; left: 661px; top: 42px; width: 106px; height: 88px; background: var(--white);
    font-size: 10px; line-height: 13px; text-align: center; color: #222; padding-top: 10px;
  }
  .indicia b { font-weight: 700; }

  .address-block {
    position: absolute; left: 235px; top: 235px; width: 240px; height: 64px;
    border: 1.5px solid var(--ink-grey); font-size: 12px; font-weight: 700; color: #222;
    padding: 6px 0 0 20px; line-height: 17px;
  }
  .address-block__route { padding-left: 14px; letter-spacing: .3px; }

  .sender { position: absolute; left: 160px; top: 328px; display: flex; align-items: flex-start; gap: 24px; }
  .sender__mark { width: 38px; height: 38px; border-radius: 50%; background: var(--green-mid); margin-top: 6px; }
  .sender__name { font-family: "Oswald", sans-serif; font-weight: 500; font-size: 18px; color: var(--ink-green); text-transform: uppercase; }
  .sender__line { font-size: 15px; color: var(--ink-grey); text-transform: uppercase; margin-top: 3px; letter-spacing: .2px; }

  .cta {
    position: absolute; left: 408px; top: 79px; width: 330px; height: 81px; background: var(--white);
    border-radius: 40px; text-align: center; font-family: "Oswald", sans-serif; color: var(--ink-green);
    box-shadow: 0 2px 6px rgba(0,0,0,.25); padding-top: 8px;
  }
  .cta__main { font-size: 36px; font-weight: 500; line-height: 40px; }
  .cta__sub { font-size: 17px; font-weight: 500; line-height: 20px; }

  .benefit {
    position: absolute; font-family: "Oswald", sans-serif; font-weight: 600; color: var(--ink-green);
    text-transform: uppercase; text-align: center; line-height: 1;
  }
  .benefit--treatments { left: 90px; top: 270px; width: 320px; font-size: 26px; }
  .benefit--treatments span { display: block; font-size: 31px; margin-top: 2px; }
  .benefit--spraying { left: 90px; top: 360px; width: 320px; font-size: 26px; }

  .partner { position: absolute; left: 548px; top: 305px; display: flex; align-items: center; gap: 10px; }
  .partner__mark { width: 16px; height: 16px; background: var(--ink-green); }
  .partner__name { font-family: "Oswald", sans-serif; font-weight: 500; font-size: 44px; color: var(--ink-green); line-height: 1; }
</style>
</head>
<body>

<section class="postcard postcard--front">
  <svg class="postcard__art" width="776" height="423" viewBox="0 0 776 423">
    <defs>
      <linearGradient id="front-band" x1="0" y1="0" x2="1" y2="0">
        <stop offset="0" stop-color="var(--green-deep)"/>
        <stop offset=".55" stop-color="var(--green-light)"/>
        <stop offset="1" stop-color="var(--green-mid)"/>
      </linearGradient>
      <radialGradient id="leaf-glow" cx=".5" cy=".5" r=".5">
        <stop offset="0" stop-color="var(--mint)" stop-opacity=".9"/>
        <stop offset="1" stop-color="var(--mint)" stop-opacity="0"/>
      </radialGradient>
    </defs>
    <path d="M0 0 H776 V140 C600 150 420 205 260 200 C150 196 60 180 0 172 Z" fill="url(#front-band)"/>
    <path d="M0 172 C60 180 150 196 260 200 C420 205 600 150 776 140" fill="none" stroke="var(--curve)" stroke-width="5"/>
    <ellipse cx="680" cy="300" rx="130" ry="120" fill="url(#leaf-glow)" role="img" aria-label="Faint leaf pattern decoration"/>
  </svg>
  <h1 class="headline headline--lead">Tired of the sticky mess insects leave</h1>
  <p class="headline headline--question">While damaging your valuable trees?</p>
  <p class="headline headline--offer">Now offering a complete line of environmentally<br>safe tree care products</p>
  <div class="indicia">PRSRT STD<br>ECRWSS<br>U.S.POSTAGE<br><b>PAID</b><br>EDDM RETAIL</div>
  <div class="address-block">
    <div class="address-block__route">*************ECRWSS****</div>
    <div>Local</div>
    <div>Postal Customer</div>
  </div>
  <div class="sender">
    <div class="sender__mark"></div>
    <div>
      <div class="sender__name">Hollis's Lawn Care</div>
      <div class="sender__line">Dale Hollis Licensed &amp; Certified Applicatior</div>
      <div class="sender__line">530-555-0142 hollislc@example.com</div>
    </div>
  </div>
</section>

<section class="postcard postcard--back">
  <svg class="postcard__art" width="776" height="423" viewBox="0 0 776 423">
    <defs>
      <linearGradient id="back-band" x1="0" y1="0" x2="1" y2="0">
        <stop offset="0" stop-color="var(--green-mid)"/>
        <stop offset=".6" stop-color="var(--green-light)"/>
        <stop offset="1" stop-color="var(--green-deep)"/>
      </linearGradient>
    </defs>
    <path d="M0 0 H776 V200 C640 210 520 240 380 238 C260 236 140 205 0 190 Z" fill="url(#back-band)"/>
    <path d="M0 190 C140 205 260 236 380 238 C520 240 640 210 776 200" fill="none" stroke="var(--curve)" stroke-width="5"/>
    <g class="category-stripes" transform="translate(0 310) rotate(-33)">
      <rect x="-300" y="-172" width="1100" height="43" fill="var(--purple)"/>
      <rect x="-300" y="-129" width="1100" height="43" fill="var(--lime)"/>
      <rect x="-300" y="-86" width="1100" height="43" fill="var(--orange)"/>
      <rect x="-300" y="-43" width="1100" height="43" fill="var(--blue)"/>
      <g fill="var(--white)" font-family="Open Sans, Arial, sans-serif" font-size="28" font-weight="400">
        <text x="120" y="-140">INSECTICIDES</text>
        <text x="120" y="-97">FERTILIZERS</text>
        <text x="120" y="-54">FUNDICIDES</text>
        <text x="120" y="-11">ANTIBIOTICS</text>
      </g>
    </g>
  </svg>
  <div class="cta">
    <div class="cta__main">CALL OR EMAIL NOW</div>
    <div class="cta__sub">FOR YOUR TREE CARE CONSULTATION!</div>
  </div>
  <p class="benefit benefit--treatments">Curative &amp; Preventative<span>Treatments</span></p>
  <p class="benefit benefit--spraying">No Spraying Involved</p>
  <div class="partner">
    <div class="partner__mark"></div>
    <div class="partner__name">Thornel</div>
  </div>
</section>

</body>
</html>
```